Landing Page and Logo for Auto-Blogging Platform

I created a platform that allows users to start a blog for their business, hobby, charity, etc. I need a landing page where users can learn about the platform, benefits of consistent blogging, SEO value, plans/pricing, etc. The landing page needs to have multiple call to action buttons encouraging the visitor to register/sign up for a free trial.

In addition to the landing page, I need a page for users to establish the settings for their blog. This page should be a fairly simple form, intended for the user to enter a few details to set up their blog:
1. Name of Blog
2. Up to 10 topics and/or keywords the blog should focus on
3. Theme: Color-scheme and logo upload for blog.

I have attached the specifications of the platform's functionality so you can better understand how it works, plans/pricing, etc.

I also need a logo for the business. The name of the platform is PostNook.

Target Market(s)

Website owners, bloggers, business owners

Industry/Entity Type

Technology, Internet, web design

Coding

Coded - Design and coding required

Number of Pages Required

2 page

Colors
0054AA
0677BA
7BADD7
CADEEF
E8F1F8
0094D4
00A9DD
6FCCEA
C7EBF8
E9F6FB

Requirements
Must have
• Eye-catching design but fairly light on content (keep it simple and brief.)
Nice to have
• Eye-catching yet simple design, clean and easy to understand what we are offering.
Should not have
• Too much “wordy” and confusing content.

```html
<!DOCTYPE html>
<html lang="en">
<head>
<meta charset="utf-8">
<title>PostNook – Landing, Setup and Pricing</title>
<link href="https://fonts.googleapis.com/css2?family=Poppins:wght@400;500;600;700;800&display=swap" rel="stylesheet">
<style>
  :root{
    --navy:#0a3596;
    --navy-deep:#072a80;
    --blue:#0054AA;
    --blue-mid:#0677BA;
    --sky:#0094D4;
    --cyan:#00A9DD;
    --cyan-light:#6FCCEA;
    --ice:#C7EBF8;
    --white:#ffffff;
    --ink:#0b2c6e;
    --yellow:#f6d21c;
    --page:#ffffff;
  }
  *{box-sizing:border-box;margin:0;padding:0}
  html,body{width:703px;height:1200px;overflow:hidden;background:var(--page);font-family:"Poppins",sans-serif}
  .canvas{position:relative;width:703px;height:1200px}

  .brand-top{position:absolute;top:16px;left:0;width:100%;display:flex;justify-content:center;align-items:center;gap:10px}
  .brand-top .mark{width:30px;height:30px;border-radius:50%;background:var(--navy)}
  .brand-top .name{font-weight:700;font-size:30px;color:var(--navy);letter-spacing:-0.5px}

  .screen{position:absolute;left:70px;width:562px;border-radius:4px;overflow:hidden;
    background:linear-gradient(135deg,var(--navy-deep) 0%,var(--blue) 60%,#1c6fd0 100%);color:var(--white)}
  .screen-hero{top:88px;height:350px}
  .screen-setup{top:455px;height:340px}
  .screen-pricing{top:808px;height:350px}

  .nav{position:absolute;top:12px;left:18px;right:18px;height:22px;display:flex;align-items:center}
  .nav .logo{display:flex;align-items:center;gap:6px;font-weight:700;font-size:15px}
  .nav .logo .dot{width:12px;height:12px;border-radius:50%;background:var(--white)}
  .nav .links{margin-left:auto;display:flex;gap:18px;font-size:8px;align-items:center}
  .nav .links .active{font-weight:700}
  .nav .signup{margin-left:18px;background:var(--yellow);color:var(--ink);font-size:8px;font-weight:600;padding:4px 12px;border-radius:10px}

  .intro-card{position:absolute;border-radius:10px;padding:18px;color:var(--white);
    background:linear-gradient(160deg,var(--cyan-light) 0%,var(--cyan) 45%,var(--sky) 100%)}
  .tag{display:inline-block;background:var(--white);color:var(--ink);font-size:7px;font-weight:500;padding:3px 8px;border-radius:8px}
  .intro-card h1,.intro-card h2{font-weight:700;line-height:1.15;margin-top:10px}
  .intro-card h1{font-size:17px}
  .intro-card h2{font-size:16px}
  .intro-card p{font-size:7.6px;line-height:1.45;margin-top:8px;opacity:.95}

  .cta{display:inline-flex;align-items:center;gap:10px;background:var(--white);color:var(--ink);
    font-size:8px;font-weight:600;padding:3px 3px 3px 12px;border-radius:14px}
  .cta .arrow{width:20px;height:20px;border-radius:50%;background:var(--yellow);display:flex;align-items:center;justify-content:center}

  .hero-card{left:18px;top:62px;width:270px;height:250px}
  .hero-card .cta{margin-top:22px}
  .hero-photo{position:absolute;left:240px;top:50px;width:304px;height:270px;border-radius:70px 10px 70px 10px;
    background:linear-gradient(150deg,#dfe6ee 0%,#9fb3c8 45%,#5d6f86 100%)}

  .setup-card{left:18px;top:62px;width:245px;height:250px}
  .setup-form{position:absolute;left:290px;top:66px;width:254px}
  .field{margin-bottom:11px}
  .field label{display:block;font-size:8px;font-weight:600;margin-bottom:4px}
  .field .input{background:var(--white);border-radius:4px;height:18px}
  .field .input.tall{height:40px}
  .field .input.upload{height:26px;display:flex;align-items:center;justify-content:center}

  .plans{position:absolute;left:18px;top:56px;right:18px;display:flex;gap:14px}
  .plan{position:relative;flex:1;height:276px;border-radius:10px;padding:20px 14px 14px;
    background:linear-gradient(170deg,var(--cyan-light) 0%,var(--cyan) 40%,var(--blue-mid) 100%)}
  .plan.featured{background:linear-gradient(170deg,var(--sky) 0%,var(--blue) 100%);border:1.5px solid var(--cyan-light)}
  .plan .badge{position:absolute;top:-7px;right:12px;background:var(--yellow);color:var(--ink);font-size:7px;font-weight:600;padding:2px 8px;border-radius:8px}
  .plan h3{font-size:13px;font-weight:700}
  .plan .price{font-size:22px;font-weight:800;margin-top:2px;letter-spacing:-0.5px}
  .plan .note{font-size:7px;margin-top:4px}
  .plan .note b{font-weight:700}
  .plan ul{list-style:none;margin-top:38px}
  .plan li{display:flex;align-items:center;gap:6px;font-size:7px;margin-bottom:6px}
  .plan .cta{position:absolute;left:14px;bottom:14px;font-size:7.5px;gap:18px}
</style>
</head>
<body>
<div class="canvas">

  <header class="brand-top">
    <span class="mark"></span>
    <span class="name">PostNook</span>
  </header>

  <!-- Landing hero -->
  <section class="screen screen-hero">
    <nav class="nav">
      <div class="logo"><span class="dot"></span>PostNook</div>
      <div class="links"><span>Home</span><span>Services</span><span>Pricing</span><span class="active">Set Up</span><span>About</span></div>
      <span class="signup">Sign up</span>
    </nav>
    <div class="hero-photo" role="img" aria-label="Photo of hands typing on a laptop at a bright desk"></div>
    <div class="intro-card hero-card">
      <span class="tag">#StartYourBlog</span>
      <h1>Start Your Blog with Ease: Empower Your Passion, Business, or Cause</h1>
      <p>Create a blog in minutes. Perfect for businesses, hobbies, or charities. Share your story and connect with your audience effortlessly. Get started today!</p>
      <span class="cta">Start free trial
        <span class="arrow"><svg width="9" height="9" viewBox="0 0 10 10"><path d="M1 5h7M5 2l3 3-3 3" fill="none" stroke="#0b2c6e" stroke-width="1.5" stroke-linecap="round"/></svg></span>
      </span>
    </div>
  </section>

  <!-- Blog setup -->
  <section class="screen screen-setup">
    <nav class="nav">
      <div class="logo"><span class="dot"></span>PostNook</div>
      <div class="links"><span>Home</span><span>Services</span><span>Pricing</span><span class="active">Set Up</span><span>About</span></div>
      <span class="signup">Sign up</span>
    </nav>
    <div class="intro-card setup-card">
      <span class="tag">#StartYourBlog</span>
      <h2>Set Up Your Blog: Customize and Personalize</h2>
      <p>Get your blog ready in just a few steps. Fill out the form below to name your blog, choose focus topics, and customize your theme. With these simple settings, you'll be on your way to creating a blog that truly represents you and your brand.</p>
    </div>
    <form class="setup-form">
      <div class="field"><label>Blog Name</label><div class="input"></div></div>
      <div class="field"><label>Focus Topics &amp; Keywords</label><div class="input tall"></div></div>
      <div class="field"><label>Theme Customization</label><div class="input"></div></div>
      <div class="field"><label>Upload Your Logo</label>
        <div class="input upload"><svg width="16" height="12" viewBox="0 0 16 12"><path d="M4 10.5H3.5a3 3 0 0 1-.3-6A4 4 0 0 1 11 3.6a3 3 0 0 1 1.5 6.9H12M8 11V5.5M5.8 7.6 8 5.4l2.2 2.2" fill="none" stroke="#0677BA" stroke-width="1.1" stroke-linecap="round" stroke-linejoin="round"/></svg></div>
      </div>
    </form>
  </section>

  <!-- Pricing -->
  <section class="screen screen-pricing">
    <nav class="nav">
      <div class="logo"><span class="dot"></span>PostNook</div>
      <div class="links"><span>Home</span><span>Services</span><span class="active">Pricing</span><span>Set Up</span><span>About</span></div>
      <span class="signup">Sign up</span>
    </nav>
    <div class="plans">
      <article class="plan">
        <h3>Base Plan</h3>
        <div class="price">$9.99/MO</div>
        <p class="note">For <b>every month</b> you will get</p>
        <ul>
          <li><svg width="8" height="8" viewBox="0 0 10 10"><path d="M1.5 5.2 4 7.5 8.5 2.5" fill="none" stroke="#fff" stroke-width="1.6" stroke-linecap="round"/></svg>1 blog post</li>
          <li><svg width="8" height="8" viewBox="0 0 10 10"><path d="M1.5 5.2 4 7.5 8.5 2.5" fill="none" stroke="#fff" stroke-width="1.6" stroke-linecap="round"/></svg>Up to 1,000 words</li>
        </ul>
        <span class="cta">SUBSCRIBE NOW<span class="arrow"><svg width="9" height="9" viewBox="0 0 10 10"><path d="M1 5h7M5 2l3 3-3 3" fill="none" stroke="#0b2c6e" stroke-width="1.5" stroke-linecap="round"/></svg></span></span>
      </article>
      <article class="plan featured">
        <span class="badge">#Loaded</span>
        <h3>Premium Plan</h3>
        <div class="price">$14.99/MO</div>
        <p class="note">For <b>every week</b> you will get</p>
        <ul>
          <li><svg width="8" height="8" viewBox="0 0 10 10"><path d="M1.5 5.2 4 7.5 8.5 2.5" fill="none" stroke="#fff" stroke-width="1.6" stroke-linecap="round"/></svg>1 blog post</li>
          <li><svg width="8" height="8" viewBox="0 0 10 10"><path d="M1.5 5.2 4 7.5 8.5 2.5" fill="none" stroke="#fff" stroke-width="1.6" stroke-linecap="round"/></svg>Up to 2,000 words</li>
        </ul>
        <span class="cta">SUBSCRIBE NOW<span class="arrow"><svg width="9" height="9" viewBox="0 0 10 10"><path d="M1 5h7M5 2l3 3-3 3" fill="none" stroke="#0b2c6e" stroke-width="1.5" stroke-linecap="round"/></svg></span></span>
      </article>
      <article class="plan">
        <h3>Ultimate Plan</h3>
        <div class="price">$24.99/MO</div>
        <p class="note">For <b>every day</b> you will get</p>
        <ul>
          <li><svg width="8" height="8" viewBox="0 0 10 10"><path d="M1.5 5.2 4 7.5 8.5 2.5" fill="none" stroke="#fff" stroke-width="1.6" stroke-linecap="round"/></svg>1 blog post</li>
          <li><svg width="8" height="8" viewBox="0 0 10 10"><path d="M1.5 5.2 4 7.5 8.5 2.5" fill="none" stroke="#fff" stroke-width="1.6" stroke-linecap="round"/></svg>Up to 2,000 words</li>
          <li><svg width="8" height="8" viewBox="0 0 10 10"><path d="M1.5 5.2 4 7.5 8.5 2.5" fill="none" stroke="#fff" stroke-width="1.6" stroke-linecap="round"/></svg>Unlimited manual posting</li>
        </ul>
        <span class="cta">SUBSCRIBE NOW<span class="arrow"><svg width="9" height="9" viewBox="0 0 10 10"><path d="M1 5h7M5 2l3 3-3 3" fill="none" stroke="#0b2c6e" stroke-width="1.5" stroke-linecap="round"/></svg></span></span>
      </article>
    </div>
  </section>

</div>
</body>
</html>
```